Classy, Elegant, Simple Business Card Design

Looking to have a classy, simple, and elegant design. Want a top notch designed business card. I really like the look of the new veltro credit card. I also like the design I attached. I am trying to reach 21-29 year old females for booking us for there wedding or event. We offer Disc Jockey Service, Photo Booth Rentals, and Uplighting .

Target Market(s)

21-28 year old females

Contact Information for Business Card

Has to have logo, website, email, and phone number

Font styles to use
Other font styles liked:
• open to font choice, modern, clean
Designer to choose
33a6d7
0791cd
0555a3
ffffff

Requirements
Must have
• Has to have logo, website, email, and phone number
Nice to have
• I really like the design of the new veltro credit card. I also included my logo and some designs I like
Should not have
• clutter or too much info

```html
<!DOCTYPE html>
<html lang="en">
<head>
<meta charset="utf-8">
<title>Lumora Events — Business Card</title>
<link href="https://fonts.googleapis.com/css2?family=Poppins:wght@300;500&display=swap" rel="stylesheet">
<style>
  :root {
    --backdrop: #d8d3cb;
    --card: #ffffff;
    --sky: #33a6d7;
    --blue: #0791cd;
    --navy: #0555a3;
    --ink: #6f6f6f;
    --icon: #5e5e5e;
  }
  * { margin: 0; padding: 0; box-sizing: border-box; }
  html, body {
    width: 1200px;
    height: 800px;
    overflow: hidden;
    background: var(--backdrop);
    font-family: "Poppins", sans-serif;
  }
  .stage {
    width: 1200px;
    height: 800px;
    display: flex;
    align-items: center;
    justify-content: center;
  }
  .business-card {
    position: relative;
    width: 700px;
    height: 400px;
    background: var(--card);
    box-shadow: 0 20px 40px rgba(0, 0, 0, 0.12);
  }
  .brand {
    position: absolute;
    left: 64px;
    top: 92px;
    display: flex;
    align-items: center;
    gap: 12px;
  }
  .brand-dot {
    width: 16px;
    height: 16px;
    border-radius: 50%;
    background: var(--blue);
  }
  .brand-name {
    font-weight: 500;
    font-size: 24px;
    letter-spacing: 0.04em;
    color: var(--navy);
  }
  .contact-list {
    position: absolute;
    left: 420px;
    top: 262px;
    list-style: none;
  }
  .contact-item {
    display: flex;
    align-items: center;
    gap: 14px;
    height: 30px;
    font-weight: 300;
    font-size: 17px;
    color: var(--ink);
  }
  .contact-icon {
    width: 16px;
    height: 16px;
    flex: none;
    fill: var(--icon);
  }
</style>
</head>
<body>
  <main class="stage">
    <section class="business-card" aria-label="Lumora Events business card">
      <div class="brand">
        <span class="brand-dot"></span>
        <span class="brand-name">LUMORA EVENTS</span>
      </div>
      <ul class="contact-list">
        <li class="contact-item">
          <svg class="contact-icon" viewBox="0 0 16 16" aria-hidden="true">
            <path d="M4 0h8a1.5 1.5 0 0 1 1.5 1.5v13A1.5 1.5 0 0 1 12 16H4a1.5 1.5 0 0 1-1.5-1.5v-13A1.5 1.5 0 0 1 4 0zm0 2v11h8V2z"/>
          </svg>
          <span>310-555-0182</span>
        </li>
        <li class="contact-item">
          <svg class="contact-icon" viewBox="0 0 16 16" aria-hidden="true">
            <path d="M0 3h16v10H0zm1.5 1.5v.4L8 9l6.5-4.1v-.4zm0 2.2v4.8h13V6.7L8 10.8z"/>
          </svg>
          <span>hello@lumoraevents.com</span>
        </li>
        <li class="contact-item">
          <svg class="contact-icon" viewBox="0 0 16 16" aria-hidden="true">
            <path d="M8 0a8 8 0 1 0 0 16A8 8 0 0 0 8 0zm5.9 7.2h-2.6a12 12 0 0 0-1-4.8 6.4 6.4 0 0 1 3.6 4.8zM8 1.7c.8 1 1.5 3 1.7 5.5H6.3C6.5 4.7 7.2 2.7 8 1.7zM5.7 2.4a12 12 0 0 0-1 4.8H2.1a6.4 6.4 0 0 1 3.6-4.8zM2.1 8.8h2.6a12 12 0 0 0 1 4.8 6.4 6.4 0 0 1-3.6-4.8zM8 14.3c-.8-1-1.5-3-1.7-5.5h3.4c-.2 2.5-.9 4.5-1.7 5.5zm2.3-.7a12 12 0 0 0 1-4.8h2.6a6.4 6.4 0 0 1-3.6 4.8z"/>
          </svg>
          <span>www.lumoraevents.com</span>
        </li>
      </ul>
    </section>
  </main>
</body>
</html>
```